Need posters that inspire entrepreneurs

I want to create beautiful, inspiring wall art. I'm looking for a designer to create an awesome sample (note this sample is not for real use). The winning design will form the foundation of our art "style" so there will be LOTS of ongoing work for the winning designer.

It's your challenge to create a style that is clean, inspiring and timeless, and possibly can be adapted to different colour palettes.

Looking for a perfect execution of words, image and design.

The attached example shows one idea. It should serve as an idea only.

Format of the images should be either rectangular or square. Exact size is preferably UK A4 (US letter) or max A3. Assume that a display would consist of a 4 x 4 image grid so size needs to allow for that in a small to medium size office.

The quotes I want in the 3 samples (each in an individual poster - not combined in 1 poster). Each quote should have it's own, the reason for three is to prove the design work on more than one quote. The quotes are:

1) Failure is the condiment that gives success its flavor.
– Dorian Welsby

2) Whether you think you can or think you can’t, you’re right.
– Oswald Pike

3) Ever tried. Ever failed. No matter. Try Again. Fail again. Fail better.
– Lionel Marwick

Each design should include the image of the person and the quote + any design elements you consider relevant. You should find relevant images of the individuals being quoted. The final images will not be published or used commercially in any way.

Font styles to use
Serif
Sans Serif

Colors

Designer to choose colors to be used in the design.

Requirements
Must have
• Words and headshot image - 1 per poster design.
• Please consider in the design that there will not always be photographs of the person quoted and as such the design will need to hold, whether the source is a photo, sketch or something else.
Nice to have
• None, but note that the final image will be printed on a wall mounted board, printed to the edge but not on the edge. The board will have black or white edges so consider in the design.
Should not have
• None

```html
<!DOCTYPE html>
<html lang="en">
<head>
<meta charset="utf-8">
<title>Fail Better – Quote Poster</title>
<link href="https://fonts.googleapis.com/css2?family=Barlow+Condensed:wght@500;600&display=swap" rel="stylesheet">
<style>
  :root {
    --backdrop: #e8e5e0;
    --board-edge: #3a3a3c;
    --paper: #ffffff;
    --ink: #4a4a4c;
    --slate: #565658;
    --slate-dark: #3f3f41;
    --hairline: #d6d6d8;
    --blue-light: #1c93dc;
    --blue-deep: #08479a;
    --photo-light: #b9b9b9;
    --photo-mid: #8a8a8a;
    --photo-dark: #4e4e50;
  }
  * { margin: 0; padding: 0; box-sizing: border-box; }
  html, body {
    width: 1200px;
    height: 900px;
    overflow: hidden;
    background: var(--backdrop);
  }
  .canvas {
    position: relative;
    width: 1200px;
    height: 900px;
  }
  .poster {
    position: absolute;
    left: 40px;
    top: 53px;
    width: 1120px;
    height: 794px;
    display: block;
  }
  .quote-line {
    font-family: "Barlow Condensed", "Arial Narrow", sans-serif;
    font-weight: 600;
    font-size: 48px;
    fill: var(--ink);
  }
  .author-name {
    font-family: "Barlow Condensed", "Arial Narrow", sans-serif;
    font-weight: 500;
    font-size: 23px;
    fill: var(--paper);
  }
</style>
</head>
<body>
<main class="canvas">
  <svg class="poster" viewBox="0 0 858 608" xmlns="http://www.w3.org/2000/svg">
    <defs>
      <radialGradient id="portrait-tone" cx="0.55" cy="0.4" r="0.75">
        <stop offset="0" stop-color="var(--photo-light)"/>
        <stop offset="0.55" stop-color="var(--photo-mid)"/>
        <stop offset="1" stop-color="var(--photo-dark)"/>
      </radialGradient>
      <linearGradient id="portrait-fade" x1="0" y1="0" x2="1" y2="0">
        <stop offset="0" stop-color="#ffffff" stop-opacity="1"/>
        <stop offset="1" stop-color="#ffffff" stop-opacity="0"/>
      </linearGradient>
      <linearGradient id="blue-band" x1="0" y1="0" x2="1" y2="1">
        <stop offset="0" stop-color="var(--blue-light)"/>
        <stop offset="1" stop-color="var(--blue-deep)"/>
      </linearGradient>
      <linearGradient id="slate-band" x1="0" y1="0" x2="1" y2="0">
        <stop offset="0" stop-color="var(--slate-dark)"/>
        <stop offset="1" stop-color="var(--slate)"/>
      </linearGradient>
    </defs>

    <!-- board edge and white margin -->
    <rect class="board-edge" x="0" y="0" width="858" height="608" fill="var(--board-edge)"/>
    <rect class="paper-margin" x="9" y="9" width="840" height="590" fill="var(--paper)"/>

    <!-- artwork area -->
    <g class="artwork">
      <rect x="16" y="12" width="825" height="583" fill="var(--paper)"/>

      <g class="portrait" role="img" aria-label="Black and white portrait photograph of Lionel Marwick">
        <rect x="440" y="12" width="401" height="583" fill="url(#portrait-tone)"/>
        <rect x="440" y="12" width="70" height="583" fill="url(#portrait-fade)"/>
      </g>

      <g class="hairlines" stroke="var(--hairline)" stroke-width="0.8">
        <line x1="16" y1="60" x2="130" y2="12"/>
        <line x1="16" y1="78" x2="172" y2="12"/>
        <line x1="16" y1="96" x2="214" y2="12"/>
        <line x1="16" y1="114" x2="256" y2="12"/>
        <line x1="16" y1="132" x2="298" y2="12"/>
        <line x1="16" y1="150" x2="340" y2="12"/>
        <line x1="470" y1="440" x2="841" y2="330" opacity="0.6"/>
        <line x1="480" y1="450" x2="841" y2="345" opacity="0.6"/>
        <line x1="490" y1="460" x2="841" y2="360" opacity="0.6"/>
      </g>

      <polygon class="slate-band" points="16,378 16,595 400,595 450,574" fill="url(#slate-band)"/>
      <g class="slate-stripes" stroke="var(--paper)" stroke-width="3">
        <line x1="16" y1="389" x2="460" y2="571"/>
        <line x1="16" y1="398" x2="446" y2="575"/>
      </g>

      <polygon class="blue-band" points="396,595 841,404 841,595" fill="url(#blue-band)"/>
    </g>

    <!-- quote -->
    <g class="quote">
      <text class="quote-line" x="79" y="130" textLength="317" lengthAdjust="spacingAndGlyphs">Ever tried. Ever failed.</text>
      <text class="quote-line" x="79" y="189" textLength="298" lengthAdjust="spacingAndGlyphs">No matter. Try Again.</text>
      <text class="quote-line" x="79" y="248" textLength="311" lengthAdjust="spacingAndGlyphs">Fail again. Fail better.</text>
    </g>

    <!-- attribution bubble -->
    <g class="attribution">
      <path d="M424 338 C438 330 420 314 408 303 C440 313 456 334 449 362 Z" fill="var(--slate)"/>
      <rect x="223" y="336" width="226" height="42" rx="21" fill="var(--slate)"/>
      <text class="author-name" x="336" y="364" text-anchor="middle">Lionel Marwick</text>
    </g>
  </svg>
</main>
</body>
</html>
```